Process Roadmap for Interior Design Firm

We are looking to ramp up the design appeal of our current process roadmap to be very visually interesting, while staying informative and descriptive about our process.

Target Market(s)

In-house Clients

Industry/Entity Type

Interior Design Firm focused on sustainable and holistic design.

Other font styles liked:
• raleway

Requirements
Must have
• 1.) it would be nice if the graphic provided a more clear indication of the “journey” from one step to the next, so that there was a clear sense of the progression (such that we are directing the viewer) 2.). We would want it to fit on an 8.5”x11” page (the page could be horizontal when we have the Steady Pathway formatted out with the testimonials) (in addition to the testimonials, we may also want to have the detailed descriptions of each step of the process presented below the graphic, so that the graphic is cleaner) 3.) ideally the graphic is clear and simple enough to also be used on our Bi-Weekly Client Updates, which will be typed updates for clients re their project budgets, schedule and scope. The Steady Pathway graphic (without all the testimonials) would be at the end of the update, and would fit on the page horizontally at the bottom, perhaps in a space which is 7.5”w x 4”h or so.
Should not have
• bold or bright colors. Natural neutrals are preferred, such as the ones featured on the provided graphic.

```html
<!DOCTYPE html>
<html lang="en">
<head>
<meta charset="utf-8">
<title>KLR Steady Pathway</title>
<link href="https://fonts.googleapis.com/css2?family=Raleway:wght@400;500;700;800&family=Open+Sans:wght@400;700&display=swap" rel="stylesheet">
<style>
  :root {
    --backdrop: #c3b99a;
    --paper: #fffdd6;
    --ink-dark: #57574a;
    --ink-text: #2f2e28;
    --title-grey: #4d4d48;
    --card-sand: #c5bc9d;
    --card-linen: #d8d0b0;
    --card-mist: #e3e0c8;
    --card-shadow: #6c6c68;
    --chevron: #c5bc9d;
    --label-text: #ffffff;
  }
  * { margin: 0; padding: 0; box-sizing: border-box; }
  html, body { width: 1200px; height: 1000px; overflow: hidden; }
  body { background: var(--backdrop); font-family: "Raleway", sans-serif; position: relative; }

  .sheet { position: absolute; left: 166px; top: 159px; width: 880px; height: 679px; background: var(--paper); }

  .name-banner { position: absolute; left: 255px; top: 0; width: 371px; height: 189px; }
  .name-banner svg { position: absolute; inset: 0; }
  .firm-name {
    position: absolute; left: 0; right: 0; top: 22px; text-align: center;
    font-family: "Raleway", sans-serif; font-weight: 700; font-size: 96px; line-height: 1;
    color: var(--paper); letter-spacing: 1px;
  }

  .pathway-title {
    position: absolute; left: 0; right: 0; top: 207px; text-align: center;
    font-family: "Raleway", sans-serif; font-weight: 400; font-size: 29px;
    letter-spacing: 6px; color: var(--title-grey);
  }

  .steps { position: absolute; left: 16px; top: 284px; width: 860px; height: 230px; list-style: none; }
  .step { position: absolute; top: 0; width: 116px; height: 170px; }
  .step-card {
    position: absolute; inset: 0; border-radius: 16px;
    box-shadow: 6px 6px 0 var(--card-shadow);
    padding: 36px 7px 0; text-align: center;
    font-family: "Open Sans", sans-serif; font-size: 10.3px; line-height: 12.4px; color: var(--ink-text);
  }
  .step--sand .step-card { background: var(--card-sand); }
  .step--linen .step-card { background: var(--card-linen); }
  .step--mist .step-card { background: var(--card-mist); }
  .step-label { position: absolute; left: 16px; top: 0; width: 84px; height: 32px; }
  .step-label svg { position: absolute; inset: 0; }
  .step-label span {
    position: absolute; left: 0; right: 0; top: 9px; text-align: center;
    font-family: "Open Sans", sans-serif; font-weight: 700; font-size: 11px; color: var(--label-text);
  }
  .step-arrow { position: absolute; top: 191px; left: 33px; width: 50px; height: 32px; }
</style>
</head>
<body>
  <main class="sheet">
    <header class="name-banner">
      <svg width="371" height="189" viewBox="0 0 371 189" aria-hidden="true">
        <polygon points="0,0 371,0 371,108 186,189 0,108" fill="var(--ink-dark)"/>
      </svg>
      <div class="firm-name">KLR</div>
    </header>

    <h1 class="pathway-title">STEADY PATHWAY</h1>

    <ol class="steps">
      <li class="step step--sand" style="left:0">
        <div class="step-card">Listening to our clients, their land, and their home. Identifying their needs, challenges, wishes, and dreams</div>
        <div class="step-label"><svg viewBox="0 0 84 32" width="84" height="32" aria-hidden="true"><polygon points="0,0 84,0 84,20 42,32 0,20" fill="var(--ink-dark)"/></svg><span>LISTENING</span></div>
        <svg class="step-arrow" viewBox="0 0 50 32" aria-hidden="true"><polygon points="0,0 34,0 50,16 34,32 0,32 16,16" fill="var(--chevron)"/></svg>
      </li>
      <li class="step step--linen" style="left:122px">
        <div class="step-card">Facilitating a guided visioning process to clarify the deepest intention, true purpose, and highest potential for their home and their future within it.</div>
        <div class="step-label"><svg viewBox="0 0 84 32" width="84" height="32" aria-hidden="true"><polygon points="0,0 84,0 84,20 42,32 0,20" fill="var(--ink-dark)"/></svg><span>VISIONING</span></div>
        <svg class="step-arrow" viewBox="0 0 50 32" aria-hidden="true"><polygon points="0,0 34,0 50,16 34,32 0,32 16,16" fill="var(--chevron)"/></svg>
      </li>
      <li class="step step--mist" style="left:244px">
        <div class="step-card">Turning our client's vision into a clearly defines scope, budget, and timeline. Mapping out the steps for making their dream a reality. Setting a meeting schedule from start to finish.</div>
        <div class="step-label"><svg viewBox="0 0 84 32" width="84" height="32" aria-hidden="true"><polygon points="0,0 84,0 84,20 42,32 0,20" fill="var(--ink-dark)"/></svg><span>PLANNING</span></div>
        <svg class="step-arrow" viewBox="0 0 50 32" aria-hidden="true"><polygon points="0,0 34,0 50,16 34,32 0,32 16,16" fill="var(--chevron)"/></svg>
      </li>
      <li class="step step--sand" style="left:366px">
        <div class="step-card">Following the schedule through the design phases from initial design concepts, technical drawings and detail, and the selection of all finishes, fixtures, and surnishings.</div>
        <div class="step-label"><svg viewBox="0 0 84 32" width="84" height="32" aria-hidden="true"><polygon points="0,0 84,0 84,20 42,32 0,20" fill="var(--ink-dark)"/></svg><span>DESIGNING</span></div>
        <svg class="step-arrow" viewBox="0 0 50 32" aria-hidden="true"><polygon points="0,0 34,0 50,16 34,32 0,32 16,16" fill="var(--chevron)"/></svg>
      </li>
      <li class="step step--linen" style="left:488px">
        <div class="step-card">Coordinating with clients, builders, architects, and vendors to ensure that the design is executed with excellence, and the construction and furnishings are on-time and on-budget.</div>
        <div class="step-label"><svg viewBox="0 0 84 32" width="84" height="32" aria-hidden="true"><polygon points="0,0 84,0 84,20 42,32 0,20" fill="var(--ink-dark)"/></svg><span>MANAGING</span></div>
        <svg class="step-arrow" viewBox="0 0 50 32" aria-hidden="true"><polygon points="0,0 34,0 50,16 34,32 0,32 16,16" fill="var(--chevron)"/></svg>
      </li>
      <li class="step step--mist" style="left:610px">
        <div class="step-card">Overseeing the inspection, Installation, and arrangement of all furnishings, lighting, artwork, and decorative items. Taking care of every last detail.</div>
        <div class="step-label"><svg viewBox="0 0 84 32" width="84" height="32" aria-hidden="true"><polygon points="0,0 84,0 84,20 42,32 0,20" fill="var(--ink-dark)"/></svg><span>INSTALLING</span></div>
        <svg class="step-arrow" viewBox="0 0 50 32" aria-hidden="true"><polygon points="0,0 34,0 50,16 34,32 0,32 16,16" fill="var(--chevron)"/></svg>
      </li>
      <li class="step step--sand" style="left:732px">
        <div class="step-card">Fixing any issues of defects. Follow up on all remaining items. Completing the final finishing touches to our client's full and total satisfaction.</div>
        <div class="step-label"><svg viewBox="0 0 84 32" width="84" height="32" aria-hidden="true"><polygon points="0,0 84,0 84,20 42,32 0,20" fill="var(--ink-dark)"/></svg><span>COMPLETING</span></div>
        <svg class="step-arrow" viewBox="0 0 50 32" aria-hidden="true"><polygon points="0,0 34,0 50,16 34,32 0,32 16,16" fill="var(--chevron)"/></svg>
      </li>
    </ol>
  </main>
</body>
</html>
```